Sproutlab 3.0 - Educational Guide/Course-pack/Worksheet

Our Sproutlab 3.0 toolkit is an educational workshop that focuses on inspiring student initiatives in the classroom! We need a new educational course guide or course-pack for students/teachers that clearly outlines or explains the program steps, offers helpful tips and includes empty spaces/lines where their can write down their great ideas or notes. This will include a;

- Teachers Guide (1 Page)
- Student Guide/Worksheet (4 Pages)
- Group Pack Resources (3 Pages)

This will consist of designing/formatting text, stock animation/icons, font, etc. We have included our new logo (color, branding, etc.) and all of the text for each separate course-pack. We have also attached our new website to give you an idea of the program style.

Our workshop can be for any school project like Technology, Community, Environment, Art, Science, etc.

Target Market(s)

High School Students/Teachers

Industry/Entity Type

Education

Font styles to use
Sans Serif

Colors
f68e4e
acd037
34a7d8

Requirements
Must have
• Use our brand colors from logo.
Should not have
• Should not be too childish.

```html
<!DOCTYPE html>
<html lang="en">
<head>
<meta charset="utf-8">
<title>Sproutlab 3.0 – Student Guide</title>
<link href="https://fonts.googleapis.com/css2?family=Lato:wght@400;700;900&family=Libre+Baskerville:wght@700&display=swap" rel="stylesheet">
<style>
:root{
  --green:#6a9d3c;
  --green-line:#7fae4e;
  --ink:#2a2a2a;
  --blue:#1f8ec3;
  --backdrop:#e9e9ea;
  --paper:#ffffff;
  --photo-dark:#2a1f17;
  --photo-mid:#5b4a3c;
}
*{box-sizing:border-box;margin:0;padding:0}
html,body{width:1200px;height:436px;overflow:hidden;background:var(--backdrop)}
body{position:relative;font-family:'Lato',sans-serif;color:var(--ink)}
.page{position:absolute;top:17px;width:587px;height:831px;background:var(--paper);transform:scale(0.465);transform-origin:0 0;box-shadow:0 4px 14px rgba(0,0,0,.12);overflow:hidden}
.page-1{left:23px}.page-2{left:317px}.page-3{left:607px}.page-4{left:901px}
.page-bar{position:absolute;left:0;right:0;bottom:0;height:12px;background:var(--blue)}
.t{position:absolute;font-size:8.5px;line-height:1.75;white-space:nowrap}
.t.bold{font-weight:900}
.t.q{font-weight:700}
.green{color:var(--green)}
.bullet::before{content:"";display:inline-block;width:4px;height:4px;border-radius:50%;background:var(--green);margin-right:6px;vertical-align:middle}
.sub::before{content:"";display:inline-block;width:4px;height:4px;border-radius:50%;border:1px solid var(--green);margin-right:5px;vertical-align:middle}
.rule{position:absolute;height:1px;background:var(--green-line)}
.section-tab{position:absolute;left:0;height:24px;background:var(--green);color:#fff;font-family:'Libre Baskerville',serif;font-weight:700;font-size:13px;line-height:24px;padding-left:14px;letter-spacing:.2px;white-space:nowrap}
.section-icon{position:absolute;width:34px;height:34px;border-radius:50%;background:var(--green);border:2px solid #fff;box-shadow:0 0 0 1px var(--green)}
.section-icon svg{width:100%;height:100%}
.brand-small{position:absolute;right:14px;top:40px;display:flex;align-items:center;gap:5px;font-size:12px;font-weight:700;color:#555}
.brand-small .dot{width:12px;height:12px;border-radius:2px;background:var(--green)}
.hero-photo{position:absolute;left:0;top:0;width:587px;height:269px;background:linear-gradient(180deg,var(--photo-dark) 0%,#3b2e24 45%,var(--photo-mid) 100%)}
.hero-brand{position:absolute;left:0;right:0;top:62px;display:flex;justify-content:center;align-items:center;gap:10px;color:#fff}
.hero-brand .dot{width:18px;height:18px;border-radius:3px;background:var(--green)}
.hero-brand .name{font-size:26px;font-weight:700;line-height:1}
.name-box{position:absolute;width:236px;height:96px;border:1.5px solid var(--green-line);border-radius:18px;padding:10px 20px;font-size:8.5px}
.cat{position:absolute;display:flex;align-items:center;gap:8px;font-size:8.5px}
.cat b{width:20px;height:20px;border-radius:50%;background:var(--green);color:#fff;font-size:7.5px;display:flex;align-items:center;justify-content:center}
.num{position:absolute;left:50px;font-size:8.5px;width:18px;text-align:right}
.person-photo{position:absolute;left:306px;top:483px;width:180px;height:336px;background:linear-gradient(180deg,#f3ece6 0%,#d9a6b4 40%,#8aa6c4 100%);border-radius:80px 80px 0 0}
</style>
</head>
<body>

<section class="page page-1">
  <div class="hero-photo" role="img" aria-label="Photo of graduating students in caps and gowns celebrating"></div>
  <div class="hero-brand"><span class="dot"></span><span class="name">Sproutlab 3.0</span></div>
  <div class="section-tab" style="top:301px;width:150px">1. ME AND WE</div>
  <div class="section-icon" style="left:142px;top:296px"><svg viewBox="0 0 34 34"><rect x="10" y="11" width="14" height="10" fill="none" stroke="#fff" stroke-width="1.5"/><line x1="8" y1="23" x2="26" y2="23" stroke="#fff" stroke-width="1.5"/></svg></div>
  <div class="t bold bullet" style="left:14px;top:335px">ME</div>
  <div class="t sub" style="left:14px;top:350px">List some of your talents abilities, and interests.</div>
  <div class="t sub" style="left:14px;top:365px">Think about private classes, sports, hobbies, music, computers, things you like, things you know how to do.</div>
  <div class="rule" style="left:37px;width:236px;top:406px"></div><div class="rule" style="left:313px;width:236px;top:406px"></div>
  <div class="rule" style="left:37px;width:236px;top:432px"></div><div class="rule" style="left:313px;width:236px;top:432px"></div>
  <div class="rule" style="left:37px;width:236px;top:458px"></div><div class="rule" style="left:313px;width:236px;top:458px"></div>
  <div class="rule" style="left:37px;width:236px;top:485px"></div><div class="rule" style="left:313px;width:236px;top:485px"></div>
  <div class="t bold bullet" style="left:14px;top:522px">WE</div>
  <div class="t sub" style="left:14px;top:536px">List the talents, abilities, and interests of each of your group members.</div>
  <div class="name-box" style="left:38px;top:570px">Name :</div>
  <div class="name-box" style="left:313px;top:570px">Name :</div>
  <div class="name-box" style="left:38px;top:686px">Name :</div>
  <div class="name-box" style="left:313px;top:686px">Name :</div>
  <div class="page-bar"></div>
</section>

<section class="page page-2">
  <div class="section-tab" style="top:38px;width:204px">2. THE BRAINSTORM</div>
  <div class="section-icon" style="left:198px;top:33px"><svg viewBox="0 0 34 34"><circle cx="17" cy="16" r="7" fill="none" stroke="#fff" stroke-width="1.5"/></svg></div>
  <div class="brand-small"><span class="dot"></span>Sproutlab 3.0</div>
  <div class="t" style="left:14px;top:78px">Find some project ideas! Here are 3 easy ways to do it!</div>
  <div class="t sub" style="left:14px;top:95px">Use what you wrote in part 1 to give you ideas!</div>
  <div class="t sub" style="left:14px;top:110px">What does your school need, what problems could you solve, what would be great to have?</div>
  <div class="t sub" style="left:14px;top:125px">These categories might help!</div>
  <div class="cat" style="left:38px;top:154px"><b>A</b>Relationship Building</div>
  <div class="cat" style="left:177px;top:154px"><b>C</b>Education</div>
  <div class="cat" style="left:276px;top:154px"><b>E</b>Sports</div>
  <div class="cat" style="left:385px;top:154px"><b>G</b>Health</div>
  <div class="cat" style="left:468px;top:154px"><b>I</b>Environment</div>
  <div class="cat" style="left:38px;top:189px"><b>B</b>Entertainment</div>
  <div class="cat" style="left:177px;top:189px"><b>D</b>Arts</div>
  <div class="cat" style="left:276px;top:189px"><b>F</b>Technology</div>
  <div class="cat" style="left:385px;top:189px"><b>H</b>Media</div>
  <div class="cat" style="left:468px;top:189px"><b>J</b>Social Justice</div>
  <div class="t q" style="left:14px;top:235px">List activities, businesses, products, or services that would work well in your school or community.</div>
  <div class="num" style="top:268px">1.</div><div class="rule" style="left:75px;width:458px;top:278px"></div>
  <div class="num" style="top:291px">2.</div><div class="rule" style="left:75px;width:458px;top:301px"></div>
  <div class="num" style="top:314px">3.</div><div class="rule" style="left:75px;width:458px;top:324px"></div>
  <div class="num" style="top:337px">4.</div><div class="rule" style="left:75px;width:458px;top:347px"></div>
  <div class="num" style="top:360px">5.</div><div class="rule" style="left:75px;width:458px;top:370px"></div>
  <div class="num" style="top:383px">6.</div><div class="rule" style="left:75px;width:458px;top:393px"></div>
  <div class="num" style="top:406px">7.</div><div class="rule" style="left:75px;width:458px;top:416px"></div>
  <div class="num" style="top:429px">8.</div><div class="rule" style="left:75px;width:458px;top:439px"></div>
  <div class="num" style="top:452px">9.</div><div class="rule" style="left:75px;width:458px;top:462px"></div>
  <div class="num" style="top:475px">10.</div><div class="rule" style="left:75px;width:458px;top:485px"></div>
  <div class="section-tab" style="top:528px;width:244px">3. THE BEST OF THE BEST</div>
  <div class="section-icon" style="left:238px;top:523px"><svg viewBox="0 0 34 34"><circle cx="17" cy="15" r="6" fill="none" stroke="#fff" stroke-width="1.5"/><path d="M13 20l-2 7 6-3 6 3-2-7" fill="none" stroke="#fff" stroke-width="1.2"/></svg></div>
  <div class="t" style="left:14px;top:568px">Choose your best idea or combine some to make one!</div>
  <div class="t" style="left:14px;top:583px">Is your idea realistic, original, and useful?</div>
  <div class="t" style="left:14px;top:605px">Project Idea or Name:</div><div class="rule" style="left:104px;width:236px;top:616px"></div>
  <div class="t" style="left:14px;top:627px">Tasks:</div>
  <div class="t" style="left:14px;top:642px">List all the things you'd have to do to make this project happen.</div>
  <div class="t" style="left:14px;top:657px">Think about money, permission, production, materials, promotion, everything!</div>
  <div class="rule" style="left:37px;width:236px;top:698px"></div><div class="rule" style="left:313px;width:236px;top:698px"></div>
  <div class="rule" style="left:37px;width:236px;top:724px"></div><div class="rule" style="left:313px;width:236px;top:724px"></div>
  <div class="rule" style="left:37px;width:236px;top:750px"></div><div class="rule" style="left:313px;width:236px;top:750px"></div>
  <div class="rule" style="left:37px;width:236px;top:776px"></div><div class="rule" style="left:313px;width:236px;top:776px"></div>
  <div class="page-bar"></div>
</section>

<section class="page page-3">
  <div class="section-tab" style="top:38px;width:184px">4. THE BIG PITCH</div>
  <div class="section-icon" style="left:176px;top:33px"><svg viewBox="0 0 34 34"><path d="M11 23l6-12 6 12" fill="none" stroke="#fff" stroke-width="1.5"/></svg></div>
  <div class="brand-small"><span class="dot"></span>Sproutlab 3.0</div>
  <div class="t bold bullet" style="left:14px;top:78px">PREPARE</div>
  <div class="t sub" style="left:14px;top:93px">List all the positive points and all the challenges you may have in doing this project.</div>
  <div class="t bold" style="left:35px;top:142px">POSITIVE POINTS</div>
  <div class="t bold" style="left:312px;top:142px">CHALLENGES</div>
  <div class="rule" style="left:37px;width:236px;top:180px"></div><div class="rule" style="left:313px;width:236px;top:180px"></div>
  <div class="rule" style="left:37px;width:236px;top:206px"></div><div class="rule" style="left:313px;width:236px;top:206px"></div>
  <div class="rule" style="left:37px;width:236px;top:232px"></div><div class="rule" style="left:313px;width:236px;top:232px"></div>
  <div class="rule" style="left:37px;width:236px;top:258px"></div><div class="rule" style="left:313px;width:236px;top:258px"></div>
  <div class="t bold bullet" style="left:14px;top:308px">PRESENT</div>
  <div class="t sub" style="left:14px;top:323px">Two or more members of your team will present your project to the other groups.</div>
  <div class="t sub" style="left:14px;top:338px">Your presentation should answer these questions in an interesting, fun, or original way!</div>
  <div class="t sub" style="left:14px;top:353px">If you have time, make a poster with a visual of your slogan, logo, or ad.</div>
  <div class="t q bullet" style="left:35px;top:393px">Where did your idea come from?</div>
  <div class="rule" style="left:43px;width:506px;top:424px"></div><div class="rule" style="left:43px;width:506px;top:450px"></div>
  <div class="t q bullet" style="left:35px;top:483px">What is the idea and what will have to be done?</div>
  <div class="rule" style="left:43px;width:506px;top:514px"></div><div class="rule" style="left:43px;width:506px;top:540px"></div>
  <div class="t q bullet" style="left:35px;top:573px">What is this a good idea?</div>
  <div class="rule" style="left:43px;width:506px;top:604px"></div><div class="rule" style="left:43px;width:506px;top:630px"></div>
  <div class="t q bullet" style="left:35px;top:663px">Who will benefit from your project?</div>
  <div class="rule" style="left:43px;width:506px;top:694px"></div><div class="rule" style="left:43px;width:506px;top:720px"></div>
  <div class="t" style="left:14px;top:747px">All the other teams will look for missing details, ask questions, find problems, and offer suggestions! So be ready to defend your idea!</div>
  <div class="page-bar"></div>
</section>

<section class="page page-4">
  <div class="section-tab" style="top:38px;width:246px">5. LAUNCH THE PROJECT!</div>
  <div class="section-icon" style="left:240px;top:33px"><svg viewBox="0 0 34 34"><circle cx="17" cy="17" r="7" fill="none" stroke="#fff" stroke-width="1.5"/><circle cx="17" cy="17" r="2.5" fill="#fff"/></svg></div>
  <div class="brand-small"><span class="dot"></span>Sproutlab 3.0</div>
  <div class="t bold bullet" style="left:14px;top:78px">THE WHO'S WHO?</div>
  <div class="t sub" style="left:14px;top:93px">These are positions that are played in any project or business.</div>
  <div class="t sub" style="left:14px;top:108px">Read each description.</div>
  <div class="t sub" style="left:14px;top:123px">Match each of your group members (including you) with the position that fits best!</div>

  <div class="t" style="left:22px;top:152px"><span class="green">The Go-Getters :</span>&nbsp; Public relations and sales</div>
  <div class="rule" style="left:212px;width:310px;top:163px"></div>
  <div class="t" style="left:94px;top:167px">These people like to talk and get people's attention.</div>
  <div class="t" style="left:94px;top:182px">"Why be shy?" They promote and sell.</div>

  <div class="t" style="left:22px;top:226px"><span class="green">The Number-Crunchers :</span>&nbsp; Finance and Administration</div>
  <div class="rule" style="left:258px;width:264px;top:237px"></div>
  <div class="t" style="left:127px;top:241px">These people are organized and can keep track of money and information.</div>

  <div class="t" style="left:22px;top:285px"><span class="green">The Doers :</span>&nbsp; Production or Service provider</div>
  <div class="rule" style="left:212px;width:310px;top:296px"></div>
  <div class="t" style="left:74px;top:300px">If it's a product- they'll make it.</div>
  <div class="t" style="left:74px;top:315px">If it's a service- they'll provide it. You can count on them!</div>

  <div class="t" style="left:22px;top:359px"><span class="green">The Magicians :</span>&nbsp; Advertising and Publicity</div>
  <div class="rule" style="left:205px;width:317px;top:370px"></div>
  <div class="t" style="left:89px;top:374px">They have creative ideas. They come up with cool advertisements, slogans, and posters.</div>

  <div class="t" style="left:22px;top:418px"><span class="green">The Chameleon :</span>&nbsp; Advertising and Publicity</div>
  <div class="rule" style="left:212px;width:310px;top:429px"></div>
  <div class="t" style="left:94px;top:433px">They keep track of everything that needs to be done and who needs to do it!</div>

  <div class="t green" style="left:22px;top:477px">Go :</div>
  <div class="t sub" style="left:50px;top:477px">You have a great project idea.</div>
  <div class="t sub" style="left:50px;top:492px">Now make it happen.</div>
  <div class="t sub" style="left:50px;top:507px">Your idea will probably change.</div>
  <div class="t sub" style="left:50px;top:522px">Just keep moving forward.</div>

  <div class="t bold bullet" style="left:14px;top:566px">THE G-PACK</div>
  <div class="t sub" style="left:14px;top:582px">Use the tools in it to help you.</div>

  <div class="person-photo" role="img" aria-label="Photo of a smiling student holding notebooks and giving a thumbs up"></div>
  <div class="page-bar"></div>
</section>

</body>
</html>
```